Design and Renovation Company Luxury Business Card

I want to create a luxury business card for a Design and Renovation Firm . We will use our current logo. The company name is 742KAVO. We do not want anything standard. We need a very unique concept.
Please see uploaded inspiration. I really like the textured paper option. I would like the card to be thick with debossing, and/or embossing options. The logo has orange in it but I would like to see the card with and without the orange. I think the orange may make the company feel less high-end. The goal is to elevate the logo not match its vibe per se of the logo. We want something very unique, not standard at all!
I would like a space for :
Logo,
Name,
Position,
Email,
Office number,
Website Address,
Business Address,
Thank you!
Have fun!
Target Market(s)
Home owners Age 35 +
Industry/Entity Type
Design and Renovation
Contact Information for Business Card
Logo, Name, Position, Email, Office number, Website Address, Business Address,.
Colors
Designer to choose colors to be used in the design.
Requirements
Must have
- A luxury designer feel. Must be black or dark grey but open to other luxury ideas.
Nice to have
- Gold, silver, black embossing or debossing. Textured paper design.
Should not have
- A cheap look and feel.

```html
<!DOCTYPE html>
<html lang="en">
<head>
<meta charset="utf-8">
<title>742KAVO Business Card</title>
<link rel="stylesheet" href="https://fonts.googleapis.com/css2?family=Open+Sans:wght@400;600;700&display=swap">
<style>
  :root {
    --stage: #d9d4cc;
    --ink: #111111;
    --paper: #ffffff;
    --accent: #f7941d;
    --text: #1c1c1c;
    --back-dark: #0c0c0c;
    --back-light: #4a4a4a;
  }
  * { margin: 0; padding: 0; box-sizing: border-box; }
  html, body { width: 900px; height: 1200px; overflow: hidden; }
  body {
    background: var(--stage);
    font-family: "Open Sans", Arial, sans-serif;
    position: relative;
  }
  .card {
    position: absolute;
    left: 80px;
    width: 742px;
    height: 442px;
    border-radius: 22px;
    overflow: hidden;
  }
  .card-front { top: 130px; background: var(--paper); }
  .card-back { top: 637px; background: var(--back-dark); }

  .front-band {
    position: absolute;
    left: 0;
    right: 0;
    top: 340px;
    bottom: 0;
    background: linear-gradient(180deg, #2a2a2a 0%, var(--ink) 100%);
  }

  .brand-name {
    position: absolute;
    font-weight: 600;
    line-height: 1;
    white-space: nowrap;
  }
  .front-brand { left: 73px; top: 200px; font-size: 40px; color: var(--ink); letter-spacing: 2px; }
  .back-brand { left: 283px; top: 280px; font-size: 58px; color: var(--paper); letter-spacing: 3px; }

  .contact-block {
    position: absolute;
    left: 369px;
    top: 120px;
    padding-left: 13px;
    border-left: 2px solid var(--accent);
    color: var(--text);
    height: 200px;
  }
  .person-name { font-size: 26px; font-weight: 700; color: var(--accent); line-height: 1.1; margin-top: -2px; }
  .person-role { font-size: 17px; margin-top: 5px; }
  .address { font-size: 17px; line-height: 20px; margin-top: 15px; }
  .contact-list { list-style: none; margin-top: 14px; }
  .contact-list li { display: flex; align-items: center; font-size: 17px; height: 28px; }
  .contact-icon { width: 16px; height: 16px; margin-right: 9px; flex: none; }

  .back-pattern {
    position: absolute;
    inset: 0;
    background: linear-gradient(90deg, var(--back-dark) 0%, #1a1a1a 45%, var(--back-light) 100%);
  }
</style>
</head>
<body>
  <section class="card card-front">
    <div class="front-band" role="img" aria-label="Dark decorative band along the lower edge of the card"></div>

    <p class="brand-name front-brand">742KAVO</p>

    <div class="contact-block">
      <p class="person-name">Daniel Brooks</p>
      <p class="person-role">Managing Director</p>
      <p class="address">418 Alder Grove Rd, #115<br>Fairmont, OH 430417</p>
      <ul class="contact-list">
        <li>
          <svg class="contact-icon" viewBox="0 0 16 16" aria-hidden="true"><path d="M3.5 1.5l2.5 0 1 3.5-1.7 1.2c.8 1.8 2.3 3.3 4 4l1.2-1.7 3.5 1v2.5c0 .8-.7 1.5-1.5 1.5C6.8 13.5 2.5 9.2 2 3c0-.8.7-1.5 1.5-1.5z" fill="var(--accent)"/></svg>
          555-318-0427
        </li>
        <li>
          <svg class="contact-icon" viewBox="0 0 16 16" aria-hidden="true"><rect x="1.5" y="3.5" width="13" height="9" rx="1" fill="var(--accent)"/><path d="M1.8 4l6.2 4.6L14.2 4" fill="none" stroke="var(--paper)" stroke-width="1.2"/></svg>
          info@your websitename.com
        </li>
        <li>
          <svg class="contact-icon" viewBox="0 0 16 16" aria-hidden="true"><circle cx="8" cy="8" r="6.5" fill="var(--accent)"/><path d="M1.5 8h13M8 1.5c-2.5 3-2.5 10 0 13M8 1.5c2.5 3 2.5 10 0 13" fill="none" stroke="var(--paper)" stroke-width="1"/></svg>
          www.your websitename.com
        </li>
      </ul>
    </div>
  </section>

  <section class="card card-back">
    <div class="back-pattern" role="img" aria-label="Embossed square texture fading from black on the left to grey on the right"></div>
    <p class="brand-name back-brand">742KAVO</p>
  </section>
</body>
</html>
```